Postcard Flyer For Plumbing Company

We are a p[professional plumbing company in NSW that carry out plumbing, electrical and hot water system work.
i want to send a postcard size flyer 105mm x 148mm to our clients to offer $xx off their next job they book with us.
The front of the flyer needs to say.... Feel The Love WIth $35 Off your Next Job. It needs to include a section where their name and postal address can go (74mm W x 24mm H) on the left hand side of the bottom of the flyer - refer attached example.
The other side of the flyer needs to have a section for text, the offer ($35 or $xx what they get off their next job) and also can use the tag line... Call 1 Number for The Best In 3 Trades - Plumbing, Hot Water & Electrical.
Plumbing, hot water and electrical pictures/icons can be used.
I want the flyer to stand out, use the corporate colours and be modern whilst letting them know that they can use this voucher on their next job.
Refer attachments.

Target Market(s)

Homeowners and our existing clients

Industry/Entity Type

Plumbing

Font styles to use
Serif

Colors
0255a3
ec1f27
ffffff
d3d3d3

Requirements
Must have
• Corporate colours and logos
• Red Colour:
• C=0
• M=100
• Y=100
• K=0
• Blue Colour
• C= 100
• M=66
• Y=0
• K=2
• Grey Colour
• C= 26
• M=21
• Y=19
• K=0
Nice to have
• predominately white background
Should not have
• Black background and lots of black.

```html
<!DOCTYPE html>
<html lang="en">
<head>
<meta charset="utf-8">
<title>Harlow Trades – Postcard Flyer</title>
<link href="https://fonts.googleapis.com/css2?family=Baloo+2:wght@600;700;800&family=Hind:wght@400;500;600&display=swap" rel="stylesheet">
<style>
  :root{
    --brand-blue:#0255a3;
    --brand-red:#ec1f27;
    --deep-red:#8e1a1f;
    --white:#ffffff;
    --light-grey:#d3d3d3;
    --mid-grey:#9a9a9a;
    --charcoal:#3a3a3a;
    --ink:#333333;
  }
  *{margin:0;padding:0;box-sizing:border-box}
  html,body{width:774px;height:1200px;overflow:hidden;background:var(--white)}
  body{font-family:"Hind",sans-serif;color:var(--ink)}
  .postcard{position:relative;width:774px;height:1200px;overflow:hidden;background:var(--white)}

  /* ---------- front side ---------- */
  .front{position:absolute;left:0;top:0;width:774px;height:600px}
  .front-backdrop{position:absolute;left:0;top:0;width:774px;height:442px;
    background:linear-gradient(135deg,#f2f2f2 0%,#e0e0e0 40%,#ededed 70%,#d9d9d9 100%)}
  .worker-photo{position:absolute;left:488px;top:0;width:286px;height:442px;
    background:linear-gradient(180deg,#bdbdbd 0%,#7a7a7a 30%,#2f2f2f 60%,#6d6d6d 100%)}
  .trade-photo{position:absolute;top:45px;width:100px;height:100px}
  .trade-photo.electrical{left:261px;background:linear-gradient(135deg,#8a8a8a,#3e3e3e)}
  .trade-photo.plumbing{left:369px;background:linear-gradient(135deg,#f0f0f0,#b9b9b9 60%,#d5532c)}
  .trade-photo.hotwater{left:478px;background:linear-gradient(135deg,#5a5a5a,#d8d8d8 50%,#222)}

  .tile{position:absolute}
  .tile.red{background:var(--brand-red)}
  .tile.deep{background:var(--deep-red)}
  .tile.blue{background:var(--brand-blue)}
  .tile.dark{background:var(--charcoal)}
  .tile.grey{background:var(--mid-grey)}
  .tile.soft{opacity:.75}

  .headline{position:absolute;left:158px;top:182px;font-family:"Baloo 2",sans-serif;font-weight:800;
    font-size:34px;line-height:30px;color:var(--charcoal);letter-spacing:-1px}
  .headline .accent{color:var(--brand-red)}
  .offer{position:absolute;left:128px;top:250px;font-family:"Baloo 2",sans-serif;font-weight:800;color:var(--charcoal);
    white-space:nowrap}
  .offer .currency{font-size:38px;color:var(--brand-red);vertical-align:top;position:relative;top:14px}
  .offer .amount{font-size:84px;letter-spacing:-4px;line-height:1}
  .offer .off-your{font-size:36px;font-style:italic;font-weight:700;margin-left:4px}
  .next-job{position:absolute;left:136px;top:318px;font-family:"Baloo 2",sans-serif;font-weight:800;
    font-size:74px;line-height:1;letter-spacing:-3px;color:var(--brand-red)}

  .brand{font-family:"Baloo 2",sans-serif;font-weight:800;color:var(--brand-blue);letter-spacing:1px;line-height:1}
  .front-brand{position:absolute;left:530px;top:468px;width:220px;text-align:center;font-size:38px}
  .front-brand .mark{display:inline-block;width:14px;height:14px;background:var(--brand-red);margin-right:8px;vertical-align:middle}
  .services{font-family:"Hind",sans-serif;font-weight:600;font-size:14px;color:var(--ink)}
  .front-services{position:absolute;left:530px;top:554px;width:220px;text-align:center}

  /* ---------- back side ---------- */
  .back{position:absolute;left:0;top:600px;width:774px;height:600px}
  .back-backdrop{position:absolute;left:148px;top:0;width:626px;height:444px;
    background:linear-gradient(135deg,#f7f7f7 0%,#e9e9e9 50%,#f3f3f3 100%)}
  .water-photo{position:absolute;left:0;top:0;width:148px;height:150px;
    background:linear-gradient(135deg,#0b4f9c 0%,#5fa8e6 50%,#1a5fae 100%)}
  .tradesman-photo{position:absolute;left:18px;top:110px;width:122px;height:334px;
    background:linear-gradient(180deg,#e9d2c0 0%,#1f2e5a 20%,#23305e 85%,#4a3426 100%);border-radius:30px 30px 4px 4px}

  .web{position:absolute;right:26px;top:24px;font-size:21px;color:var(--mid-grey);display:flex;align-items:center;gap:6px}
  .web .domain{color:var(--brand-blue)}
  .tagline{position:absolute;left:158px;top:66px;font-family:"Baloo 2",sans-serif;font-weight:700;font-size:27px;
    letter-spacing:-.5px;color:var(--brand-blue);line-height:1}
  .trades{position:absolute;left:158px;top:100px;font-family:"Baloo 2",sans-serif;font-weight:800;font-size:34px;
    letter-spacing:-1px;color:var(--brand-red);line-height:1}
  .offer-note{position:absolute;left:160px;top:150px;font-size:20px;color:var(--ink)}
  .offer-note b{font-weight:600}

  .features{position:absolute;top:200px;list-style:none;width:220px}
  .features.col-a{left:160px}
  .features.col-b{left:414px}
  .features li{position:relative;padding-left:22px;font-size:13.4px;line-height:16px;margin-bottom:8px;color:var(--ink)}
  .features li svg{position:absolute;left:0;top:2px}

  .contact-band{position:absolute;left:0;top:444px;width:774px;height:156px;background:var(--brand-blue)}
  .back-brand{position:absolute;left:28px;top:34px;width:200px;text-align:center;font-size:34px;color:var(--white)}
  .back-brand .mark{display:inline-block;width:12px;height:12px;background:var(--brand-red);margin-right:8px;vertical-align:middle}
  .back-services{position:absolute;left:26px;top:112px;color:var(--white)}
  .back-services .dot{color:var(--brand-red)}
  .contact{position:absolute;left:476px;list-style:none;color:var(--white)}
  .contact li{position:absolute;left:0;display:flex;gap:12px;white-space:nowrap}
  .contact .address{top:20px;font-size:16px;line-height:18px}
  .contact .phone{top:72px;font-size:20px;font-weight:600}
  .contact .email{top:104px;font-size:16px}
  .contact svg{flex:none;margin-top:2px}
</style>
</head>
<body>
<main class="postcard">

  <section class="front">
    <div class="front-backdrop" role="img" aria-label="Faded plumbing pipes, taps and plans background"></div>
    <div class="worker-photo" role="img" aria-label="Tradesman in checked shirt carrying a toolbox"></div>
    <div class="trade-photo electrical" role="img" aria-label="Electrical switchboard work"></div>
    <div class="trade-photo plumbing" role="img" aria-label="Wrench on sink pipe"></div>
    <div class="trade-photo hotwater" role="img" aria-label="Chrome tap handle"></div>

    <div class="tile red" style="left:84px;top:148px;width:64px;height:64px"></div>
    <div class="tile deep soft" style="left:84px;top:212px;width:32px;height:30px"></div>
    <div class="tile dark soft" style="left:0;top:242px;width:32px;height:32px"></div>
    <div class="tile grey soft" style="left:32px;top:242px;width:32px;height:32px"></div>
    <div class="tile blue" style="left:32px;top:274px;width:84px;height:84px"></div>
    <div class="tile dark soft" style="left:0;top:274px;width:32px;height:32px"></div>
    <div class="tile red" style="left:84px;top:358px;width:32px;height:32px"></div>
    <div class="tile grey soft" style="left:0;top:358px;width:32px;height:64px"></div>
    <div class="tile dark soft" style="left:116px;top:390px;width:32px;height:32px"></div>
    <div class="tile dark" style="left:166px;top:406px;width:54px;height:54px"></div>
    <div class="tile red" style="left:55px;top:438px;width:31px;height:31px"></div>
    <div class="tile red" style="left:0;top:0;width:26px;height:24px"></div>
    <div class="tile deep soft" style="left:730px;top:170px;width:44px;height:44px"></div>
    <div class="tile deep" style="left:700px;top:262px;width:34px;height:34px"></div>
    <div class="tile dark soft" style="left:676px;top:294px;width:18px;height:18px"></div>
    <div class="tile dark soft" style="left:630px;top:356px;width:38px;height:38px"></div>
    <div class="tile deep soft" style="left:700px;top:408px;width:36px;height:34px"></div>

    <h1 class="headline">Feel The<br><span class="accent">Love</span> With</h1>
    <p class="offer"><span class="currency">$</span><span class="amount">35</span><span class="off-your">off your</span></p>
    <p class="next-job">Next Job.</p>

    <p class="brand front-brand"><span class="mark"></span>HARLOW<br>TRADES</p>
    <p class="services front-services">Plumbing • Electrical • Hot Water</p>
  </section>

  <section class="back">
    <div class="back-backdrop" role="img" aria-label="Faded tap and pipe background"></div>
    <div class="water-photo" role="img" aria-label="Tap with running water"></div>
    <div class="tradesman-photo" role="img" aria-label="Smiling plumber in navy overalls holding a wrench"></div>

    <div class="tile dark" style="left:696px;top:100px;width:38px;height:38px"></div>
    <div class="tile red" style="left:732px;top:173px;width:42px;height:42px"></div>
    <div class="tile grey soft" style="left:675px;top:294px;width:19px;height:19px"></div>
    <div class="tile deep" style="left:701px;top:294px;width:34px;height:34px"></div>
    <div class="tile grey soft" style="left:701px;top:377px;width:34px;height:33px"></div>
    <div class="tile grey soft" style="left:668px;top:410px;width:33px;height:34px"></div>
    <div class="tile deep" style="left:701px;top:410px;width:34px;height:34px"></div>

    <p class="web">
      <svg width="13" height="13" viewBox="0 0 14 14" aria-hidden="true"><circle cx="7" cy="7" r="6" fill="none" stroke="#9a9a9a" stroke-width="1.2"/><ellipse cx="7" cy="7" rx="2.6" ry="6" fill="none" stroke="#9a9a9a" stroke-width="1"/><line x1="1" y1="7" x2="13" y2="7" stroke="#9a9a9a"/></svg>
      <span>www.<span class="domain">yourweb.com</span></span>
    </p>
    <h2 class="tagline">Call 1 Number for The Best In 3 Trades</h2>
    <p class="trades">Plumbing, Hot Water &amp; Electrical.</p>
    <p class="offer-note">(<b>$35</b> or <b>$xx</b> what they get off their next job)</p>

    <ul class="features col-a">
      <li><svg width="14" height="12" viewBox="0 0 14 12"><path d="M1 6 L5 10 L13 1" fill="none" stroke="#0255a3" stroke-width="2.4"/></svg>Lorem ipsum dolor sit amet, consectetur adipiscing elit.</li>
      <li><svg width="14" height="12" viewBox="0 0 14 12"><path d="M1 6 L5 10 L13 1" fill="none" stroke="#0255a3" stroke-width="2.4"/></svg>Sed eu libero vitae arcu tristique ornare nec ut augue.</li>
      <li><svg width="14" height="12" viewBox="0 0 14 12"><path d="M1 6 L5 10 L13 1" fill="none" stroke="#0255a3" stroke-width="2.4"/></svg>Donec lobortis ligula vel diam condimentum interdum.</li>
      <li><svg width="14" height="12" viewBox="0 0 14 12"><path d="M1 6 L5 10 L13 1" fill="none" stroke="#0255a3" stroke-width="2.4"/></svg>Phasellus vel ante vehicula, commodo odio ut, consequat tortor.</li>
      <li><svg width="14" height="12" viewBox="0 0 14 12"><path d="M1 6 L5 10 L13 1" fill="none" stroke="#0255a3" stroke-width="2.4"/></svg>Integer nec quam quis purus porta lacinia et non libero.</li>
    </ul>
    <ul class="features col-b">
      <li><svg width="14" height="12" viewBox="0 0 14 12"><path d="M1 6 L5 10 L13 1" fill="none" stroke="#0255a3" stroke-width="2.4"/></svg>Lorem ipsum dolor sit amet, consectetur adipiscing elit.</li>
      <li><svg width="14" height="12" viewBox="0 0 14 12"><path d="M1 6 L5 10 L13 1" fill="none" stroke="#0255a3" stroke-width="2.4"/></svg>Sed eu libero vitae arcu tristique ornare nec ut augue.</li>
      <li><svg width="14" height="12" viewBox="0 0 14 12"><path d="M1 6 L5 10 L13 1" fill="none" stroke="#0255a3" stroke-width="2.4"/></svg>Donec lobortis ligula vel diam condimentum interdum.</li>
      <li><svg width="14" height="12" viewBox="0 0 14 12"><path d="M1 6 L5 10 L13 1" fill="none" stroke="#0255a3" stroke-width="2.4"/></svg>Phasellus vel ante vehicula, commodo odio ut, consequat tortor.</li>
      <li><svg width="14" height="12" viewBox="0 0 14 12"><path d="M1 6 L5 10 L13 1" fill="none" stroke="#0255a3" stroke-width="2.4"/></svg>Integer nec quam quis purus porta lacinia et non libero.</li>
    </ul>

    <footer class="contact-band">
      <p class="brand back-brand"><span class="mark"></span>HARLOW<br>TRADES</p>
      <p class="services back-services">Plumbing <span class="dot">•</span> Electrical <span class="dot">•</span> Hot Water</p>
      <ul class="contact">
        <li class="address"><svg width="12" height="16" viewBox="0 0 12 16"><path d="M6 1a5 5 0 0 1 5 5c0 4-5 9-5 9S1 10 1 6a5 5 0 0 1 5-5z" fill="#ec1f27"/><circle cx="6" cy="6" r="2" fill="#0255a3"/></svg><span>123 Street Name,<br>22150 City Name, State (123456)</span></li>
        <li class="phone"><svg width="12" height="18" viewBox="0 0 12 18"><rect x="1" y="1" width="10" height="16" rx="2" fill="#ec1f27"/><rect x="3" y="3" width="6" height="8" fill="#0255a3"/></svg><span>01234 56789</span></li>
        <li class="email"><svg width="16" height="12" viewBox="0 0 16 12"><rect x="0" y="0" width="16" height="12" fill="#ec1f27"/><path d="M0 0 L8 7 L16 0" fill="none" stroke="#0255a3" stroke-width="1.5"/></svg><span>info@yourmailhere.com</span></li>
      </ul>
    </footer>
  </section>

</main>
</body>
</html>
```